Commercial photographer, UAV drone photography & 360 walk-through visuals

I need a business card design that is minimalist but yet pretentiously creative. My target market are architects, designers, advertising agents and marketing managers. It is important to stress that though I am asking for a minimalist design it needs to have creative impact.

Target Market(s)

Architects, interiors designers, web-designers, artists

Contact Information for Business Card

Include my name, mobile [cell] number, email, web page and the company logo. Do not to include a postal address.

Colors

Designer to choose colors to be used in the design.

Requirements
Must have
• The following information is to be included:
• Milo Fenwick
• Photographer
• m: 07812 593174
• e: milo@mfimagery.co.uk
• w: mfimagery.co.uk

```html
<!DOCTYPE html>
<html lang="en">
<head>
<meta charset="utf-8">
<title>MF Imagery – Business Card</title>
<link href="https://fonts.googleapis.com/css2?family=Montserrat:wght@300;400;700&display=swap" rel="stylesheet">
<style>
  :root {
    --backdrop: #121212;
    --card: #1d1d1f;
    --card-sheen: #2a2a2c;
    --ink: #f2f2f2;
    --ink-soft: #bdbdbd;
    --rule: #d9d9d9;
  }
  * { margin: 0; padding: 0; box-sizing: border-box; }
  html, body {
    width: 1200px; height: 960px; overflow: hidden;
    background: var(--backdrop);
    font-family: "Montserrat", sans-serif;
    color: var(--ink);
  }
  .sheet {
    width: 1200px; height: 960px;
    display: flex; align-items: center; justify-content: center; gap: 60px;
  }
  .card {
    position: relative;
    width: 520px; height: 297px;
    background: linear-gradient(125deg, var(--card) 0%, var(--card-sheen) 45%, var(--card) 75%);
    box-shadow: 0 18px 40px rgba(0,0,0,.6);
    overflow: hidden;
  }
  .wordmark {
    display: flex; align-items: center; gap: 12px;
    font-weight: 300; text-transform: uppercase; letter-spacing: .18em;
    white-space: nowrap;
  }
  .wordmark__dot {
    width: 14px; height: 14px; border-radius: 50%;
    background: currentColor; flex: none;
  }
  /* Front */
  .card--front { display: flex; align-items: center; justify-content: center; }
  .card--front .wordmark { font-size: 30px; color: var(--ink-soft); }

  /* Back */
  .card--back .wordmark {
    position: absolute; left: 40px; top: 34px;
    font-size: 26px; color: var(--ink);
  }
  .divider {
    position: absolute; left: 40px; top: 170px;
    width: 380px; height: 1px; background: var(--rule);
  }
  .contacts {
    position: absolute; left: 40px; bottom: 42px;
    list-style: none; font-size: 12.5px; font-weight: 400; line-height: 1.55;
    color: var(--ink); white-space: nowrap;
  }
  .contacts li { display: flex; align-items: center; gap: 10px; }
  .contacts svg { width: 12px; height: 12px; fill: none; stroke: var(--ink); stroke-width: 1.6; flex: none; }
  .identity {
    position: absolute; right: 36px; bottom: 46px; text-align: right;
    white-space: nowrap;
  }
  .identity__name {
    font-size: 17px; font-weight: 700; letter-spacing: .16em; text-transform: uppercase;
  }
  .identity__title {
    font-size: 12px; font-weight: 400; color: var(--ink-soft);
    border-top: 1px solid var(--rule); display: inline-block;
    padding-top: 3px; margin-top: 3px; padding-left: 40px;
  }
</style>
</head>
<body>
<main class="sheet">
  <section class="card card--front" aria-label="Card front">
    <div class="wordmark"><span class="wordmark__dot"></span>MF Imagery</div>
  </section>

  <section class="card card--back" aria-label="Card back">
    <div class="wordmark"><span class="wordmark__dot"></span>MF Imagery</div>
    <div class="divider"></div>

    <ul class="contacts">
      <li>
        <svg viewBox="0 0 12 12"><path d="M2 1.5h2.2l1 2.6-1.3 1a6 6 0 0 0 3 3l1-1.3 2.6 1V10a1 1 0 0 1-1 1A8.5 8.5 0 0 1 1 2.5a1 1 0 0 1 1-1z"/></svg>
        07812 593174
      </li>
      <li>
        <svg viewBox="0 0 12 12"><rect x="1" y="2.5" width="10" height="7"/><path d="M1 2.5l5 4 5-4"/></svg>
        milo@mfimagery.co.uk
      </li>
      <li>
        <svg viewBox="0 0 12 12"><circle cx="6" cy="6" r="4.8"/><path d="M1.2 6h9.6M6 1.2c-2.4 2.8-2.4 6.8 0 9.6M6 1.2c2.4 2.8 2.4 6.8 0 9.6"/></svg>
        mfimagery.co.uk
      </li>
    </ul>

    <div class="identity">
      <div class="identity__name">Milo Fenwick</div>
      <div class="identity__title">Photographer</div>
    </div>
  </section>
</main>
</body>
</html>
```